Harrowgate Building and Property Services needs a business card design

We need a business card design for our building and property services business. We already have a logo we just need a creative design and layout on a business card. Emphasis on clean, modern, professional.
Our client targets are mainly body corporates, building managers, construction managers.
We are a building services company that lean more to structural repair of buildings, through concrete rectification and carbon fibre strengthening.
We also refurbish facades, rendering, painting etc
We target higher end body corporates in prestigious locations, hence why we'd like our cards to reflect professionalism, strength, efficiency

Target Market(s)

body corporates, building managers, construction managers

Industry/Entity Type

Construction

Contact Information for Business Card

Harrowgate is the main word, with 'Building and Property Services' underneath.
Level 17, 88 Marsh Lane
ELMSWORTH
Melbourne
Vic 3942
T: 9218 5371
Duncan Hensley - Director
dunharrowgate@mailbox-example.net

Requirements
Must have
• Stand out on the back of the card- strong/ bold, company logo
• All of the contact details written above
Should not have
• I'd like the card to stand out, especially on the back. Id like the company logo to be prominent, although feel free to be creative around it. But remain clean and professional

```html
<!DOCTYPE html>
<html lang="en">
<head>
<meta charset="utf-8">
<title>Harrowgate Building and Property Services – Business Card</title>
<link rel="stylesheet" href="https://fonts.googleapis.com/css2?family=Arimo:wght@400&family=Cinzel:wght@400&display=swap">
<style>
  :root {
    --backdrop: #e7e3dc;
    --card-black: #030306;
    --glow-blue: #1a1f6e;
    --brand-blue: #2f9bd8;
    --label-blue: #3f8fd9;
    --text-white: #f2f4f7;
    --rule-grey: #8c8f96;
    --subtitle-grey: #b9bec6;
  }
  * { box-sizing: border-box; margin: 0; padding: 0; }
  html, body {
    width: 1200px; height: 900px; overflow: hidden;
    background: var(--backdrop);
  }
  .sheet {
    width: 1200px; height: 900px;
    display: flex; align-items: center; justify-content: center; gap: 50px;
  }
  .card {
    position: relative;
    width: 540px; height: 309px;
    background: var(--card-black);
    border-radius: 4px;
    box-shadow: 0 10px 24px rgba(0,0,0,0.28);
    overflow: hidden;
  }

  /* Front: contact side */
  .card-front {
    background:
      radial-gradient(circle at 24% 56%, var(--glow-blue) 0%, rgba(20,24,90,0.35) 22%, var(--card-black) 48%),
      var(--card-black);
  }
  .front-mark {
    position: absolute; left: 40px; top: 128px;
    display: flex; align-items: center; gap: 10px;
  }
  .front-mark .mark-dot {
    width: 14px; height: 14px; border-radius: 50%;
    background: var(--brand-blue);
  }
  .front-mark .mark-name {
    font-family: "Cinzel", serif; font-size: 26px; letter-spacing: 2px;
    color: var(--brand-blue);
  }
  .contact {
    position: absolute; left: 300px; top: 34px; width: 220px;
    font-family: "Arimo", Arial, sans-serif; color: var(--text-white);
  }
  .contact-name { font-size: 20px; line-height: 1.1; }
  .contact-role { font-size: 13px; color: var(--label-blue); margin-top: 4px; }
  .rule { height: 1px; background: var(--rule-grey); margin: 10px 0 12px; width: 210px; }
  .address { font-style: normal; font-size: 13px; line-height: 1.45; }
  .line-item {
    display: flex; align-items: center; gap: 7px;
    font-size: 13px; line-height: 1.6;
  }
  .line-item svg { flex: none; }
  .email { font-size: 12px; white-space: nowrap; }

  /* Back: brand side */
  .card-back {
    background:
      radial-gradient(circle at 50% 48%, var(--glow-blue) 0%, rgba(20,24,90,0.35) 26%, var(--card-black) 56%),
      var(--card-black);
    display: flex; flex-direction: column; align-items: center; justify-content: center;
  }
  .back-mark { display: flex; align-items: center; gap: 14px; }
  .back-mark .mark-dot {
    width: 18px; height: 18px; border-radius: 50%;
    background: var(--brand-blue);
  }
  .back-mark .mark-name {
    font-family: "Cinzel", serif; font-size: 40px; letter-spacing: 4px;
    color: var(--brand-blue);
  }
  .tagline {
    margin-top: 8px;
    font-family: "Cinzel", serif; font-size: 11px; letter-spacing: 2px;
    color: var(--subtitle-grey); text-transform: uppercase;
  }
</style>
</head>
<body>
  <main class="sheet">
    <section class="card card-front" aria-label="Business card front">
      <div class="front-mark">
        <span class="mark-dot"></span>
        <span class="mark-name">Harrowgate</span>
      </div>
      <div class="contact">
        <h1 class="contact-name">Duncan Hensley</h1>
        <p class="contact-role">Director</p>
        <div class="rule"></div>
        <address class="address">
          Level 17, 88 Marsh Lane<br>
          ELMSWORTH<br>
          Melbourne<br>
          Vic 3942
        </address>
        <div class="rule"></div>
        <p class="line-item">
          <svg width="10" height="10" viewBox="0 0 10 10" aria-hidden="true"><rect width="10" height="10" rx="1.5" fill="#3f8fd9"/><path d="M3 2.5 L4.2 2.5 L4.7 3.8 L4 4.4 Q4.6 5.6 5.6 6 L6.2 5.3 L7.5 5.8 L7.5 7 Q5 7.3 3.2 5 Q2.6 3.8 3 2.5Z" fill="#fff"/></svg>
          9218 5371
        </p>
        <p class="line-item email">
          <svg width="10" height="10" viewBox="0 0 10 10" aria-hidden="true"><rect width="10" height="10" rx="1.5" fill="#3f8fd9"/><rect x="2" y="3" width="6" height="4.2" fill="none" stroke="#fff" stroke-width="0.8"/><path d="M2 3 L5 5.4 L8 3" fill="none" stroke="#fff" stroke-width="0.8"/></svg>
          dunharrowgate@mailbox-example.net
        </p>
      </div>
    </section>

    <section class="card card-back" aria-label="Business card back">
      <div class="back-mark">
        <span class="mark-dot"></span>
        <span class="mark-name">Harrowgate</span>
      </div>
      <p class="tagline">Building and Property Services</p>
    </section>
  </main>
</body>
</html>
```